Bref créative
BrightHollow Capital Partners
......putting entrepreneurs and investors together
Professional
Marcus Pellow
418 Weldon Avenue
Suite 340
Harlow Bend, OR 97512
brighthollowcap@mailvista.net
I have selected the black & red color scheme on the logo.
Angel Investors/Angel Funds
Seed/Start-up Investment
Private Equity Funds
Venture Capital Funding
Merchant Funding
Receivable/Purchase Order Funding

```html
<!DOCTYPE html>
<html lang="en">
<head>
<meta charset="utf-8">
<title>BrightHollow Capital Partners – Business Card</title>
<link href="https://fonts.googleapis.com/css2?family=PT+Serif:wght@400;700&display=swap" rel="stylesheet">
<style>
  :root {
    --stage: #e9e6e1;
    --card: #0d0d0e;
    --card-edge: #1c1c1e;
    --ink: #f2f2f2;
    --ink-soft: #c9c9c9;
    --accent: #c4161c;
    --accent-deep: #3a0a0c;
  }
  * { box-sizing: border-box; margin: 0; padding: 0; }
  html, body { width: 1200px; height: 646px; overflow: hidden; }
  body {
    background: var(--stage);
    font-family: "PT Serif", Georgia, serif;
    display: flex;
    align-items: center;
    justify-content: center;
    gap: 56px;
  }
  .card {
    position: relative;
    width: 520px;
    height: 297px;
    background: radial-gradient(ellipse at 40% 40%, var(--card-edge), var(--card) 70%);
    border-radius: 4px;
    box-shadow: 0 10px 26px rgba(0,0,0,.25);
    overflow: hidden;
    color: var(--ink);
  }
  .card__glow {
    position: absolute;
    left: -40px; bottom: -120px;
    width: 360px; height: 300px;
    background: radial-gradient(ellipse at center, var(--accent-deep), transparent 70%);
  }
  .brand {
    position: absolute;
    top: 54px;
    right: 46px;
    display: flex;
    align-items: center;
    gap: 10px;
    white-space: nowrap;
  }
  .brand__dot {
    width: 10px; height: 10px;
    border-radius: 50%;
    background: var(--accent);
  }
  .brand__name {
    font-size: 19px;
    font-weight: 700;
    letter-spacing: .5px;
    color: var(--ink);
  }

  .services {
    position: absolute;
    right: 46px; top: 100px;
    list-style: none;
    text-align: right;
    font-size: 12.5px;
    line-height: 1.6;
    color: var(--ink-soft);
  }
  .services li:last-child { margin-top: 10px; }

  .contact {
    position: absolute;
    left: 174px; top: 126px;
    font-size: 12.5px;
    line-height: 1.55;
    color: var(--ink-soft);
  }
  .contact__name {
    color: var(--accent);
    font-weight: 700;
    font-size: 15px;
    margin-bottom: 12px;
  }
  .contact__address { font-style: normal; margin-bottom: 8px; }
  .contact__line { display: flex; align-items: center; gap: 7px; }
  .contact__line svg { width: 10px; height: 10px; fill: var(--accent); flex: none; }
</style>
</head>
<body>
  <section class="card card--back" aria-label="Card back">
    <div class="card__glow"></div>
    <div class="brand">
      <span class="brand__dot"></span>
      <span class="brand__name">BrightHollow Capital Partners</span>
    </div>
    <ul class="services">
      <li>Angel Investors/Angel Funds</li>
      <li>Seed/Start-up Investment</li>
      <li>Private Equity Funds</li>
      <li>Venture Capital Funding</li>
      <li>Merchant Funding</li>
      <li>Receivable/Purchase Order Funding</li>
    </ul>
  </section>

  <section class="card card--front" aria-label="Card front">
    <div class="card__glow"></div>
    <div class="brand">
      <span class="brand__dot"></span>
      <span class="brand__name">BrightHollow Capital Partners</span>
    </div>
    <div class="contact">
      <p class="contact__name">Marcus Pellow</p>
      <address class="contact__address">
        418 Weldon Avenue<br>
        Suite 340, Harlow Bend, OR 97512
      </address>
      <p class="contact__line">
        <svg viewBox="0 0 10 10"><path d="M2 0h2l1 3-1.5 1a6 6 0 0 0 2.5 2.5L7 5l3 1v2a2 2 0 0 1-2 2A8 8 0 0 1 0 2a2 2 0 0 1 2-2z"/></svg>
        541-555-0148
      </p>
      <p class="contact__line">
        <svg viewBox="0 0 10 10"><path d="M2 0h2l1 3-1.5 1a6 6 0 0 0 2.5 2.5L7 5l3 1v2a2 2 0 0 1-2 2A8 8 0 0 1 0 2a2 2 0 0 1 2-2z"/></svg>
        541-555-0193
      </p>
      <p class="contact__line">
        <svg viewBox="0 0 10 10"><path d="M0 2h10v6H0z M0 2l5 3.5L10 2"/></svg>
        brighthollowcap@mailvista.net
      </p>
    </div>
  </section>
</body>
</html>
```